I need a design with just the number 24. must be in blue color (royal blue) should be large enough for people see must be in the center of page. Place a nice border around the page.

• Number 24 in Royal blue color

```html
<!DOCTYPE html>
<html lang="en">
<head>
<meta charset="utf-8">
<title>24</title>
<link href="https://fonts.googleapis.com/css2?family=Graduate&display=swap" rel="stylesheet">
<style>
  :root {
    --paper: #faf8e6;
    --paper-ray: #f3f0d6;
    --grid: rgba(232, 170, 160, 0.35);
    --royal: #0a14f0;
    --frame: #d9cf1e;
    --confetti-a: rgba(214, 120, 100, 0.22);
    --confetti-b: rgba(150, 175, 210, 0.20);
    --confetti-c: rgba(220, 200, 90, 0.18);
  }
  html, body {
    margin: 0;
    padding: 0;
    overflow: hidden;
  }
  .page {
    position: relative;
    width: 848px;
    height: 1200px;
    overflow: hidden;
    background:
      repeating-linear-gradient(90deg, transparent 0 106px, var(--grid) 106px 107px),
      repeating-linear-gradient(0deg, transparent 0 106px, var(--grid) 106px 107px),
      radial-gradient(circle at 50% 48%, var(--paper-ray) 0%, var(--paper) 60%);
  }
  .confetti-burst {
    position: absolute;
    left: 40px;
    top: 170px;
    width: 768px;
    height: 860px;
    border-radius: 50%;
    background:
      radial-gradient(ellipse at 30% 40%, var(--confetti-a), transparent 55%),
      radial-gradient(ellipse at 70% 55%, var(--confetti-b), transparent 55%),
      radial-gradient(ellipse at 50% 30%, var(--confetti-c), transparent 60%);
  }
  .frame {
    position: absolute;
    inset: 0;
  }
  .frame line {
    stroke: var(--frame);
    stroke-width: 2.5;
  }
  .frame circle {
    fill: var(--frame);
  }
  .frame .ring {
    fill: none;
    stroke: var(--frame);
    stroke-width: 2;
  }
  .number {
    position: absolute;
    left: 0;
    right: 0;
    top: 330px;
    margin: 0;
    text-align: center;
    font-family: "Graduate", "Arial Black", sans-serif;
    font-size: 470px;
    line-height: 1;
    letter-spacing: -10px;
    color: var(--paper);
    -webkit-text-stroke: 14px var(--royal);
    paint-order: stroke fill;
    text-shadow:
      -3px 3px 0 var(--royal), -6px 6px 0 var(--royal), -9px 9px 0 var(--royal),
      -12px 12px 0 var(--royal), -15px 15px 0 var(--royal), -18px 18px 0 var(--royal),
      -21px 21px 0 var(--royal), -24px 24px 0 var(--royal), -27px 27px 0 var(--royal),
      -30px 30px 0 var(--royal);
  }
</style>
</head>
<body>
  <main class="page">
    <div class="confetti-burst" role="img" aria-label="Burst of scattered multicoloured confetti around the number"></div>

    <svg class="frame" width="848" height="1200" viewBox="0 0 848 1200" aria-hidden="true">
      <line x1="46" y1="46" x2="321" y2="46"/>
      <line x1="527" y1="46" x2="802" y2="46"/>
      <line x1="46" y1="1151" x2="321" y2="1151"/>
      <line x1="527" y1="1151" x2="802" y2="1151"/>
      <line x1="46" y1="46" x2="46" y2="1151"/>
      <line x1="802" y1="46" x2="802" y2="1151"/>
      <circle class="ring" cx="44" cy="554" r="6"/>
      <circle cx="44" cy="583" r="8"/>
      <circle cx="44" cy="615" r="8"/>
      <circle class="ring" cx="44" cy="644" r="6"/>
      <circle class="ring" cx="804" cy="554" r="6"/>
      <circle cx="804" cy="583" r="8"/>
      <circle cx="804" cy="615" r="8"/>
      <circle class="ring" cx="804" cy="644" r="6"/>
    </svg>

    <h1 class="number">24</h1>
  </main>
</body>
</html>
```